The Yarrawin Pet Groomer

I have a logo which I designed myself ( I tried a contest and it did not work out well..not on this site) The logo needs some tweaking for example "THE" needs to be put above "YARRAWIN" in line with the D (on top)and it needs to be going across sideways.Also the dog is not exactly in the middle.
Also on the card I would like my name written in a simple running writing script
Marnie

Then in plain writing:
27B Fenwick St Yarrawin NSW 2851
Ph. 6319 5057
On the back:
Your next appointment:
...........................................

Pet bathing, clipping and styling

Pet

Must have
• The logo going across lengthways and changed a bit (as explained above)

```html
<!DOCTYPE html>
<html lang="en">
<head>
<meta charset="utf-8">
<title>The Yarrawin Pet Groomer – Business Card</title>
<link rel="stylesheet" href="https://fonts.googleapis.com/css2?family=Open+Sans:wght@400;700;800&family=Courgette&display=swap">
<style>
  :root {
    --backdrop: #e9e6e2;
    --card: #ffffff;
    --card-edge: #8a8a8a;
    --ink: #111111;
    --text-grey: #4a4a4a;
    --brand-red: #e2202b;
    --rule-dots: #9a9a9a;
    --mark-tone: #dfe7ee;
  }
  * { box-sizing: border-box; margin: 0; padding: 0; }
  html, body { width: 1200px; height: 426px; overflow: hidden; }
  body {
    background: var(--backdrop);
    font-family: "Open Sans", Arial, sans-serif;
    position: relative;
  }
  .card {
    position: absolute;
    top: 55px;
    width: 525px;
    height: 299px;
    background: var(--card);
    border: 1px solid var(--card-edge);
    overflow: hidden;
  }
  .card--front { left: 48px; }
  .card--back { left: 619px; }

  /* Front */
  .brand-name {
    position: absolute;
    top: 78px;
    left: 0;
    width: 100%;
    text-align: center;
    font-weight: 800;
    font-size: 25px;
    line-height: 34px;
    letter-spacing: 0.5px;
    color: var(--ink);
    text-transform: uppercase;
    white-space: nowrap;
  }
  .address, .phone {
    position: absolute;
    left: 0;
    width: 100%;
    text-align: center;
    font-size: 14.5px;
    line-height: 20px;
    color: var(--text-grey);
  }
  .address { top: 162px; }
  .phone { top: 203px; display: flex; justify-content: center; align-items: center; gap: 8px; }
  .phone svg { width: 13px; height: 13px; }
  .bar-accent {
    position: absolute;
    left: 0;
    top: 245px;
    width: 94px;
    height: 30px;
    background: var(--brand-red);
  }
  .bar-name {
    position: absolute;
    left: 100px;
    right: 0;
    top: 245px;
    height: 30px;
    background: var(--ink);
    color: #fff;
    font-weight: 700;
    font-size: 17px;
    display: flex;
    align-items: center;
    justify-content: center;
  }

  /* Back */
  .brand-mark {
    position: absolute;
    left: 44px;
    top: 20px;
    width: 118px;
    height: 118px;
    border-radius: 50%;
    background: radial-gradient(circle at 45% 40%, #f4f8fb, var(--mark-tone));
  }
  .services {
    position: absolute;
    left: 207px;
    top: 111px;
    font-family: "Courgette", cursive;
    font-size: 16px;
    line-height: 22px;
    color: var(--brand-red);
    white-space: nowrap;
  }
  .appointment-label {
    position: absolute;
    left: 44px;
    top: 185px;
    font-size: 11px;
    line-height: 16px;
    color: var(--brand-red);
  }
  .appointment-line {
    position: absolute;
    left: 44px;
    width: 450px;
    border-top: 1px dotted var(--rule-dots);
  }
  .appointment-line--1 { top: 217px; }
  .appointment-line--2 { top: 238px; }
  .appointment-line--3 { top: 259px; }
</style>
</head>
<body>
  <section class="card card--front" aria-label="Card front">
    <h1 class="brand-name">The Yarrawin Pet Groomer</h1>
    <p class="address">27B Fenwick St Yarrawin NSW 2851</p>
    <p class="phone">
      <svg viewBox="0 0 24 24" aria-hidden="true"><path fill="#4a4a4a" d="M6.6 10.8a15.1 15.1 0 0 0 6.6 6.6l2.2-2.2a1 1 0 0 1 1-.25 11.4 11.4 0 0 0 3.6.57 1 1 0 0 1 1 1V20a1 1 0 0 1-1 1A17 17 0 0 1 3 4a1 1 0 0 1 1-1h3.5a1 1 0 0 1 1 1c0 1.250.2 2.450.57 3.6a1 1 0 0 1-.25 1z"/></svg>
      <span>6319 5057</span>
    </p>
    <div class="bar-accent"></div>
    <div class="bar-name">Marnie</div>
  </section>

  <section class="card card--back" aria-label="Card back">
    <div class="brand-mark" role="img" aria-label="Brand illustration area"></div>
    <p class="services">Pet Bathing, Clipping and Styling</p>
    <p class="appointment-label">Your next appointment:</p>
    <div class="appointment-line appointment-line--1"></div>
    <div class="appointment-line appointment-line--2"></div>
    <div class="appointment-line appointment-line--3"></div>
  </section>
</body>
</html>
```